Packaging: Round Pail Design for Pond Dye

I need a new product packaging design for a lake and pond colorant. The current design is from the 90's, and it needs some new elements that are going to make it pop, while still looking cohesive with our line of products. Interesting title text, some graphical water elements, etc to make it appealing to the consumer.The brand is called Brivelunt. It currently comes in a liquid product (design attached). The new art will be for the dry dye product in water soluble pouches. The new design for the dry dye needs to be cohesive with the current liquid product, but look much more modern and eye-catching. Including an element that looks like a rectangular pouch gently splashing into the water would be appropriate.The round pail template is attached. The front area is where the new design is to be done. It can carry over onto the side if you choose.I have included the product title and optional marketing language in the template, that can be designed to fit into your design.There will be additional mandatory label text on the front, along with the label text on the side and back, which will be done internally.

Target Market(s)

Pond owners and lake managers

Industry/Entity Type

Water Treatment

Font styles to use
Sans Serif

Colors
33a6d7
0255a3

Requirements
Must have
• - Modern design that is cohesive with our older labels
• - Incorporate the Brivelunt brand and product name
• - Follow the pail template
Nice to have
• - Creative inclusion of some marketing claims
• - Graphical water elements (ie. rectangular pouch splashing into water)

```html
<!DOCTYPE html>
<html lang="en">
<head>
<meta charset="utf-8">
<title>Brivelunt Water Soluble Pouches – Pail Sidewall</title>
<link href="https://fonts.googleapis.com/css2?family=Montserrat:wght@600;700;800&family=Fira+Sans+Extra+Condensed:wght@400;600;700&family=Nunito:ital,wght@1,600;1,800&family=Roboto:wght@400&display=swap" rel="stylesheet">
<style>
:root{
  --navy:#0d3a6e;
  --brand-dark:#0255a3;
  --brand-light:#33a6d7;
  --swoosh-light:#4db3e2;
  --template-green:#1fae4b;
  --white:#ffffff;
  --table-gray:#8a8fa3;
  --table-pale:#b9c0d3;
  --ink:#1c1c1c;
}
*{margin:0;padding:0;box-sizing:border-box}
html,body{width:1200px;height:368px;overflow:hidden;background:var(--white)}
.canvas{position:relative;width:1200px;height:368px;overflow:hidden;background:var(--white)}
.abs{position:absolute;white-space:nowrap}

/* template annotations */
.spec-header{left:557px;top:49px;font-family:"Nunito",sans-serif;font-style:italic;font-weight:800;font-size:8.6px;color:var(--template-green)}
.spec-header span{margin-right:12px}
.spec-note{left:623px;top:66px;font-family:"Nunito",sans-serif;font-style:italic;font-weight:600;font-size:10.4px;color:var(--template-green)}
.guide-label{font-family:"Roboto",sans-serif;font-size:10.4px;color:var(--template-green);top:91px}
.guide-line{position:absolute;width:1px;background:var(--template-green)}
.dim{font-family:"Roboto",sans-serif;font-size:10px;line-height:10.5px;color:var(--template-green)}

/* label band */
.band{position:absolute;left:42px;top:108px;width:1152px;height:199px}

/* front panel */
.brand-name{left:204px;top:132px;font-family:"Montserrat",sans-serif;font-weight:800;font-size:30px;letter-spacing:.2px;color:var(--navy)}
.product-name{left:226px;top:165px;font-family:"Montserrat",sans-serif;font-weight:700;font-size:11.8px;color:var(--navy)}
.claims{font-family:"Montserrat",sans-serif;font-weight:700;font-size:9.4px;color:var(--brand-dark)}
.count{left:422px;top:254px;font-family:"Montserrat",sans-serif;font-weight:700;font-size:11.4px;line-height:13.2px;color:var(--navy)}
.sku{left:518px;top:177px;font-family:"Fira Sans Extra Condensed",sans-serif;font-weight:700;font-size:17px;color:var(--navy)}
.sku-sub{left:518px;top:195px;font-family:"Fira Sans Extra Condensed",sans-serif;font-weight:600;font-size:6.4px;line-height:8.4px;color:var(--navy)}

.front-legal{font-family:"Fira Sans Extra Condensed",sans-serif;color:var(--white)}
.ingredients{left:66px;top:230px;font-size:4px;font-weight:600;line-height:6px}
.keep-out{left:66px;top:248px;font-size:9.6px;font-weight:600}
.caution{left:66px;top:257px;font-size:14.5px;font-weight:700}
.read-all{left:66px;top:273px;font-size:4px;font-weight:600}
.net-weight{left:66px;top:285px;font-size:7px;font-weight:600}

/* back panel copy */
.copy{position:absolute;font-family:"Fira Sans Extra Condensed",sans-serif;font-size:4.1px;line-height:5.85px;color:var(--ink)}
.copy p{margin:0}
.copy .bold{font-weight:700}
.copy .center{text-align:center}
.copy .indent{padding-left:5px}
.col-info{left:594px;top:112px;width:130px}
.col-safety{left:731px;top:112px;width:134px;font-weight:600}
.storage-title{font-size:9px;line-height:10px;font-weight:700;margin:3px 0 1px}
.dose-table{position:absolute;left:594px;top:189px}
.seller{left:1110px;top:237px;font-family:"Fira Sans Extra Condensed",sans-serif;font-weight:700;font-size:3.9px;line-height:5.85px;color:var(--white);white-space:normal}
</style>
</head>
<body>
<div class="canvas">

  <div class="abs spec-header"><span>R &amp; T FABRICATORS</span><span>PAIL(4/B)</span><span>SIDEWALL Template</span><span>.5 FLEX LOCK</span><span>05-20-19</span></div>
  <div class="abs spec-note">*This pail does not need a Child Warning label.</div>

  <div class="abs guide-label" style="left:254px">CENTER</div>
  <div class="abs guide-label" style="left:303px">FRONT</div>
  <div class="abs guide-label" style="left:560px">EAR</div>
  <div class="abs guide-label" style="left:825px">CENTER</div>
  <div class="abs guide-label" style="left:874px">BACK</div>
  <div class="abs guide-label" style="left:1130px">EAR</div>
  <div class="guide-line" style="left:298px;top:83px;height:19px"></div>
  <div class="guide-line" style="left:584px;top:83px;height:19px"></div>
  <div class="guide-line" style="left:870px;top:83px;height:19px"></div>
  <div class="guide-line" style="left:1156px;top:83px;height:19px"></div>
  <div class="guide-line" style="left:298px;top:319px;height:18px"></div>
  <div class="guide-line" style="left:584px;top:319px;height:18px"></div>
  <div class="guide-line" style="left:870px;top:319px;height:18px"></div>
  <div class="guide-line" style="left:1156px;top:319px;height:18px"></div>

  <div class="abs dim" style="left:10px;top:108px">3.125<br>Print<br>Height</div>
  <div class="abs dim" style="left:1056px;top:327px;font-size:10.4px;line-height:13.5px">18.625″ Print Limit<br>19.125″ Overall</div>

  <svg class="band" viewBox="0 0 1152 199" aria-hidden="true">
    <defs>
      <linearGradient id="deepWater" x1="0" y1="0" x2="1" y2="1">
        <stop offset="0" stop-color="#0a4f98"/>
        <stop offset="1" stop-color="#1378bc"/>
      </linearGradient>
      <linearGradient id="deepWaterRight" x1="1" y1="0" x2="0" y2="1">
        <stop offset="0" stop-color="#0a4f98"/>
        <stop offset="1" stop-color="#1378bc"/>
      </linearGradient>
    </defs>
    <path d="M0 0 H98 C150 62 232 150 328 199 H0Z" fill="var(--swoosh-light)"/>
    <path d="M98 0 H104 C158 64 238 150 334 199 H328 C232 150 150 62 98 0Z" fill="#e6ecf2"/>
    <path d="M0 0 H14 C70 82 160 162 267 199 H0Z" fill="url(#deepWater)"/>
    <path d="M821 199 C905 150 992 80 1055 0 H1152 V199Z" fill="var(--swoosh-light)"/>
    <path d="M815 199 C899 150 986 80 1049 0 H1055 C992 80 905 150 821 199Z" fill="#e6ecf2"/>
    <path d="M877 199 C962 152 1040 82 1083 0 H1152 V199Z" fill="url(#deepWaterRight)"/>
    <rect x="0.5" y="0.5" width="1151" height="198" fill="none" stroke="var(--template-green)" stroke-width="1"/>
  </svg>

  <div class="abs brand-name">Brivelunt</div>
  <div class="abs product-name">Water Soluble Pouches</div>
  <div class="abs claims" style="left:243px;top:198px">Lake and Pond Colorant</div>
  <div class="abs claims" style="left:250px;top:209px">Add the right amount, every time!</div>
  <div class="abs claims" style="left:261px;top:220px">Quick and easy application</div>
  <div class="abs claims" style="left:281px;top:230px">Makes dosing simple!</div>
  <div class="abs claims" style="left:305px;top:241px">Dissolvable puch</div>
  <div class="abs count">6 watersoluble<br>pouches</div>
  <div class="abs sku">SKU NO.</div>
  <div class="abs sku-sub">PART NO.<br>ITEM NO.</div>

  <div class="abs front-legal ingredients">INGREDIENTS:<br>TOTAL.............................................100%</div>
  <div class="abs front-legal keep-out">KEEP OUT OF REACH OF CHILDREN</div>
  <div class="abs front-legal caution">CAUTION</div>
  <div class="abs front-legal read-all">Read all precautionary statements and first aid statements on back panel before use.</div>
  <div class="abs front-legal net-weight">NET WEIGHT 4 LB. (1.81 kg)</div>

  <div class="copy col-info">
    <p class="bold">PRODUCT INFORMATION</p>
    <p style="margin-top:2px;font-weight:600">Easy to use [Product Name] are a blended formulation of water soluble dyes packaged in a convenient water soluble pouch. Shade your pond a beautiful [blue][dark blue][reflective tint] year-round to improve the appearance of off-colored or murky water. This product is for use in lakes, ponds, decorative features and bodies of water with limited outflow.</p>
    <p class="bold" style="margin-top:8px">DIRECTIONS FOR USE:</p>
    <p>1. Toss in one pouch per acre-foot of water.</p>
    <p class="center">Length (ft.) x Width (ft.) x Average Depth (ft.)/43,560</p>
    <p class="center">= Acre Feet</p>
    <p class="center">Note: One Acre-foot = 326,000 gal. = 1,234m³</p>
    <p style="margin-top:53px">2. If multiple pouches are needed, space evenly around the pond. Dye will disperse</p>
    <p class="indent">evenly within several hours, depending upon water movement.</p>
    <p>3. Maintain color year-round by adding product as needed, following dilution or</p>
    <p class="indent">water exchange.</p>
    <p>Do not handle pouch with wet hands or gloves or place on wet surfaces. Chlorine or oxidizers will cause this product to fade.</p>
    <p style="margin-top:5px">WATER USE RESTRICTIONS: Allow several hours for dye to disperse before swimming, irrigating, fishing, or allowing animals to drink or enter the water. Do not apply directly to drinking water sources. When used at recommended dosage rate, treated water will not stain exposed surfaces or harm fish, waterfowl, pets or wildlife.</p>
  </div>

  <svg class="dose-table" width="130" height="48" viewBox="0 0 130 48" aria-label="Dosing chart: 1, 2 or 3 acre-feet uses 1, 2 or 3 pouches" role="img">
    <rect x="0.5" y="0.5" width="129" height="47" rx="5" fill="var(--table-gray)" stroke="#5b6077"/>
    <g font-family="Fira Sans Extra Condensed, sans-serif" font-weight="700" fill="#fff" text-anchor="middle">
      <text x="15" y="10" font-size="5.4">POND</text>
      <text x="15" y="17" font-size="5.4">VOLUME</text>
      <text x="15" y="34" font-size="5.4">HOW</text>
      <text x="15" y="41" font-size="5.4">MANY?</text>
    </g>
    <g>
      <rect x="31" y="1" width="32" height="23" fill="var(--brand-light)"/>
      <rect x="64" y="1" width="32" height="23" fill="var(--brand-light)"/>
      <path d="M97 1 H124 A5 5 0 0 1 129 6 V24 H97Z" fill="var(--brand-light)"/>
      <path d="M31 1 q4 5 8 0 q4 5 8 0 q4 5 8 0 q4 5 8 0 M64 1 q4 5 8 0 q4 5 8 0 q4 5 8 0 q4 5 8 0 M97 1 q4 5 8 0 q4 5 8 0 q4 5 8 0 q4 5 8 0" fill="#8fd0ee"/>
      <rect x="31" y="25" width="32" height="22" fill="var(--table-pale)"/>
      <rect x="64" y="25" width="32" height="22" fill="var(--table-pale)"/>
      <path d="M97 25 H129 V42 A5 5 0 0 1 124 47 H97Z" fill="var(--table-pale)"/>
    </g>
    <g font-family="Fira Sans Extra Condensed, sans-serif" font-weight="700" fill="#fff" text-anchor="middle">
      <text x="47" y="14" font-size="9">1</text><text x="47" y="21" font-size="5.6">ACRE-FT</text>
      <text x="80" y="14" font-size="9">2</text><text x="80" y="21" font-size="5.6">ACRE-FT</text>
      <text x="113" y="14" font-size="9">3</text><text x="113" y="21" font-size="5.6">ACRE-FT</text>
    </g>
    <g fill="#fff" stroke="#9aa3bb" stroke-width=".5">
      <rect x="43" y="29" width="12" height="14" transform="rotate(12 49 36)"/>
      <rect x="74" y="29" width="12" height="14" transform="rotate(12 80 36)"/>
      <rect x="80" y="30" width="12" height="14" transform="rotate(12 86 37)"/>
      <rect x="105" y="29" width="12" height="14" transform="rotate(12 111 36)"/>
      <rect x="110" y="30" width="12" height="14" transform="rotate(12 116 37)"/>
      <rect x="115" y="31" width="12" height="14" transform="rotate(12 121 38)"/>
    </g>
    <g font-family="Fira Sans Extra Condensed, sans-serif" font-weight="700" font-size="5.5" text-anchor="middle">
      <circle cx="47" cy="36" r="4" fill="var(--navy)" stroke="#fff" stroke-width=".6"/><text x="47" y="38" fill="#fff">1</text>
      <circle cx="80" cy="36" r="4" fill="var(--navy)" stroke="#fff" stroke-width=".6"/><text x="80" y="38" fill="#fff">2</text>
      <circle cx="113" cy="36" r="4" fill="var(--navy)" stroke="#fff" stroke-width=".6"/><text x="113" y="38" fill="#fff">3</text>
    </g>
  </svg>

  <div class="copy col-safety">
    <p class="bold">FIRST AID</p>
    <p>IF INHALED: Remove individual to fresh air. Seek medical attention if breathing becomes difficult or if respiratory irritation develops. IF ON SKIN OR CLOTHING: Flush skin with water for 15minutes. Take off all contaminated clothing and dispose. Seek medical attention if irritation develops. IF IN EYES: Flush eyes with plenty of water for at least 15 minutes. Seek medical attention if irritation develops. IF SWALLOWED: Immediately drink water to dilute. Seek medical attention if symptoms develop. Never give anything by mouth to an unconscious person.</p>
    <p>IN CASE OF EMERGENCY, CALL 1-800-555-0142.</p>
    <p>Have the production container with you when calling a poison control center or doctor or going for treatment.</p>
    <p style="margin-top:6px">PRECAUTIONARY STATEMENTS: May cause eye or skin irritation. Do not get in eyes, on skin or on clothing. Wear waterproof gloves when handling. Do not taste or swallow. Wash hands thoroughly with soap and water after use. Concentrated product can stain fabric and other porous surfaces. Avoid direct contact with these materials.</p>
    <p class="storage-title">STORAGE &amp; DISPOSAL:</p>
    <p style="font-weight:400">Store in cool place in closed container. Do not freeze. Freezing may cause pouch to become brittle. Keep pouches in original packaging until ready for use. Do not reuse empty [bags] [or] [pails]. Rinse empty [bag] [or] [pail], offer for recycling or dispose of according to state and local regulations.</p>
    <p style="font-weight:400">In case of spill, DO NOT ADD WATER. Gently sweep dry dye and dispose of properly. Do not reuse broom or dustpan without cleaning completely. If product has become wet, absorb water and dye with toweling and dispose of. Clean small sections at a time with a light bleach solution, until finished.</p>
  </div>

  <div class="abs seller">REG NO.<br><span style="display:block;height:3px"></span>Sold by:<br>COMPANY<br>ADDRESS<br>ADDRESS<br><span style="display:block;height:4px"></span>PHONE<br>TRADEMARK</div>

</div>
</body>
</html>
```